Website

Project to include our logo, (files attached - logo only to be included with the company name K&T Chemicals, Inc.). Visit the website to gather additional information. www.kandtchemicals-site.example.
Emphasis should be more on the trucking, (tanker trucks), and blending capabilities. See pictures on website.
Please incorporate the logo colors into the website design; particularly the darker blue and red.
Updates
I have updated the brief on this project. :)
I have just updated the brief.
The deadline is Sunday.
Please submit your final designs.
Thanks :)
Today is the last day to submit your designs.
Industry/Entity Type
It Company
Requirements
Must have
- Tank Truck picture/s and Rail Car pictures.
See this website for tank truck and rail picture (also shown below): http://freightlens.example/562/u-s-power-surge-respite-and-a-tally-says-vbt-ostrand-and-kellaway/

```html
<!DOCTYPE html>
<html lang="en">
<head>
<meta charset="utf-8">
<title>K&amp;T Chemicals, Inc.</title>
<link href="https://fonts.googleapis.com/css2?family=Open+Sans:ital,wght@0,400;0,600;1,400&display=swap" rel="stylesheet">
<style>
:root{
  --navy:#14288a;
  --text:#666;
  --dark:#333;
  --rust:#a1625d;
  --panel:#f2f2f2;
  --footer:#f4f4f4;
  --line:#e2e2e2;
  --white:#fff;
}
*{margin:0;padding:0;box-sizing:border-box}
html,body{width:1200px;height:1186px;overflow:hidden;background:var(--white);font-family:"Open Sans",sans-serif;color:var(--text)}
.page{position:relative;width:1200px;height:1186px}
.abs{position:absolute}

.phone-bar{left:832px;top:4px;width:368px;height:36px;background:#f2f2f2;clip-path:polygon(0 0,100% 0,100% 100%,30px 100%);}
.phone{left:880px;top:9px;font-size:15px;color:#555;display:flex;align-items:center;gap:7px}
.phone b{color:var(--navy);font-weight:600}
.phone .ic{width:21px;height:21px;background:#999;border-radius:3px;display:flex;align-items:center;justify-content:center}

.brand{left:132px;top:44px;display:flex;align-items:center;gap:10px}
.brand .dot{width:44px;height:44px;border-radius:50%;background:var(--navy);flex:none}
.brand span{font-size:22px;font-weight:600;color:var(--navy);line-height:26px;white-space:nowrap}

.nav{left:589px;top:91px;display:flex;font-size:13px;color:var(--dark)}
.nav a{color:inherit;text-decoration:none;position:relative}
.nav a.active{color:var(--navy);font-weight:600}
.nav a.active::before{content:"";position:absolute;left:-5px;right:-5px;top:-13px;height:4px;background:var(--navy)}
.nav i{font-style:normal;margin:0 16px;color:#555}

.hero{left:0;top:122px;width:1200px;height:436px;background:linear-gradient(180deg,#aab5c4 0%,#d8dde2 45%,#b9bcbd 75%,#8f8c84 100%)}
.caption{left:0;width:1200px;text-align:center;color:var(--white);font-size:38px;font-weight:600;letter-spacing:.5px;line-height:52px}
.caption span{background:rgba(40,40,40,.55);padding:0 16px}
.dots{left:553px;top:457px;display:flex;gap:6px}
.dots b{width:19px;height:19px;border-radius:50%;background:#3c3c3c}
.dots b.on{background:var(--navy)}

.welcome{left:130px;top:585px;width:940px;text-align:center}
.welcome h1{font-size:24px;font-weight:400;color:var(--navy);margin-bottom:6px}
.welcome p{font-size:13.5px;line-height:23px;letter-spacing:.1px}
.divider{left:130px;top:741px;width:940px;height:1px;background:var(--line)}

.h2{font-size:24px;font-weight:400;color:var(--navy)}
.services-title{left:130px;top:758px}
.services-img{left:130px;top:804px;width:220px;height:179px;background:linear-gradient(180deg,#c6d7ea 0%,#e6e8ea 40%,#bfc0bd 100%)}
.services-text{left:370px;top:799px;width:385px;font-size:13.5px;line-height:20px;letter-spacing:.1px}
.services-text p{margin-bottom:8px}
.btn{left:370px;top:1010px;width:94px;height:30px;background:var(--rust);color:var(--white);font-size:11px;display:flex;align-items:center;justify-content:center;border-radius:2px;letter-spacing:.3px}

.products{left:770px;top:765px;width:300px;height:276px;background:var(--panel);padding:8px 16px}
.products-img{width:268px;height:126px;margin-top:10px;background:linear-gradient(180deg,#7ea6d6 0%,#d7d3c8 45%,#b8b3a8 100%)}
.products p{font-size:13.5px;line-height:23px;margin-top:13px;letter-spacing:.1px}
.products a{color:#8b3d38;text-decoration:none}

.footer{left:0;top:1061px;width:1200px;height:125px;background:var(--footer)}
.foot-nav{left:130px;top:1084px;display:flex;font-size:13px;font-style:italic;color:var(--dark)}
.foot-nav .active{color:var(--navy)}
.foot-nav i{margin:0 16px;color:#555}
.copy{left:130px;top:1119px;font-size:12px;line-height:20px;color:#888}
.copy b{color:var(--navy);font-weight:400}
.social{left:917px;top:1088px;display:flex;gap:8px}
.social b{width:33px;height:33px;border-radius:4px;background:var(--navy)}
</style>
</head>
<body>
<div class="page">
  <div class="abs phone-bar"></div>
  <div class="abs phone">
    <span class="ic"><svg width="13" height="13" viewBox="0 0 24 24"><path fill="#fff" d="M6.6 10.8a15 15 0 0 0 6.6 6.6l2.2-2.2c.3-.3.7-.4 1-.2 1.1.4 2.3.6 3.6.6.6 0 1 .4 1 1V20c0 .6-.4 1-1 1A17 17 0 0 1 3 4c0-.6.4-1 1-1h3.5c.6 0 1 .4 1 1 0 1.3.2 2.5.6 3.6.1.3 0 .7-.2 1z"/></svg></span>
    Phone: <b>(800) 555-0147</b>
  </div>

  <div class="abs brand"><span class="dot"></span><span>K&amp;T<br>Chemicals, Inc.</span></div>

  <nav class="abs nav">
    <a class="active" href="#">Home</a><i>|</i><a href="#">About Us</a><i>|</i><a href="#">Our Services</a><i>|</i><a href="#">Our Products</a><i>|</i><a href="#">Contact Us</a>
  </nav>

  <div class="abs hero" role="img" aria-label="Industrial chemical plant with large white storage tanks and power lines"></div>
  <div class="abs caption" style="top:331px"><span>We Are a Manufacturers and Distributors</span></div>
  <div class="abs caption" style="top:386px"><span>of Industrial Chemicals</span></div>
  <div class="abs dots"><b class="on"></b><b></b><b></b><b></b></div>

  <section class="abs welcome">
    <h1>Welcome to Our Website</h1>
    <p>Aliquam molestie, mi et imperdiet euismod, dui purus auctor tellus, et interdum lacus lectus et ante. Sed accumsan sollicitudin sapien, sit amet adipiscing turpis gravida ac. In congue, neque ac lobortis volutpat, libero mauris varius mi, vitae suscipit ipsum ligula vitae risus. Duis aliquam nibh a dui iaculis viverra id a velit. Vivamus egestas risus in magna varius commodo. Sed semper viverra egestas. Etiam pretium porttitor lectus, vel ornare neque porta volutpat.</p>
  </section>
  <div class="abs divider"></div>

  <h2 class="abs h2 services-title">Our Services</h2>
  <div class="abs services-img" role="img" aria-label="Row of white chemical storage silos"></div>
  <div class="abs services-text">
    <p>K&amp;T Services was a division of the Harlow and Brennick Company and was established in 1979 with the initial intent of recovering the Phosphate value of co-product 35% Phosphoric Acid from aluminum anodizing. Trisodium Phosphate was derived from this process by a unique patented procedure.</p>
    <p>The assets of K&amp;T Services were purchased in September 1993 by Dale Mercer and incorporated thereafter as K&amp;T Chemicals, Inc.</p>
  </div>
  <div class="abs btn">LEARN MORE</div>

  <aside class="abs products">
    <h2 class="h2">Our Products</h2>
    <div class="products-img" role="img" aria-label="Storage tanks beside a plant building"></div>
    <p>Aliquam molestie, mi et imperdiet eui mod, dui purus auctor tellus, et interdum lacus lectus et ante... <a href="#">Read More</a></p>
  </aside>

  <footer class="abs footer"></footer>
  <div class="abs foot-nav"><span class="active">Home</span><i>|</i><span>About Us</span><i>|</i><span>Our Services</span><i>|</i><span>Our Products</span><i>|</i><span>Contact Us</span></div>
  <div class="abs copy">Copyright © 2014 <b>K &amp; T Chemicals, INC.</b><br>All rights reserved.</div>
  <div class="abs social"><b></b><b></b><b></b><b></b></div>
</div>
</body>
</html>
```